Letterhead & Greeting Card Design Project

I need a few files prepared for dynamic digital printing: letterhead and 2 postcards with an envelope for each. Enclosed are specific directions from the printer for each file and overall. I have also enclosed mockups of what I would like on those designs and some raw files to work with.

Industry/Entity Type

Digital

```html
<!DOCTYPE html>
<html lang="en">
<head>
<meta charset="utf-8">
<title>Letterhead Envelope</title>
<link rel="stylesheet" href="https://fonts.googleapis.com/css2?family=Titillium+Web:wght@400&display=swap">
<style>
  :root {
    --paper: #ffffff;
    --ink: #1e1e1e;
    --accent-grey: #a9a9a9;
    --accent-blue: #7fc6e2;
  }
  html, body {
    margin: 0;
    padding: 0;
    overflow: hidden;
    background: var(--paper);
  }
  .envelope {
    position: relative;
    width: 1200px;
    height: 444px;
    background: var(--paper);
    overflow: hidden;
    font-family: "Titillium Web", "Helvetica Neue", Arial, sans-serif;
    color: var(--ink);
  }
  .address {
    position: absolute;
    margin: 0;
    font-style: normal;
    font-size: 22px;
    line-height: 26px;
    font-weight: 400;
  }
  .address span { display: block; }
  .address--sender { left: 26px; top: 16px; }
  .address--recipient { left: 470px; top: 176px; }
  .brand-motif {
    position: absolute;
    left: 0;
    top: 336px;
    width: 165px;
    height: 108px;
    background: linear-gradient(120deg, var(--accent-grey) 0%, var(--accent-grey) 45%, var(--accent-blue) 75%);
    opacity: 0.55;
    border-radius: 0 60px 0 0;
  }
</style>
</head>
<body>
  <main class="envelope">
    <address class="address address--sender">
      <span>John Doe</span>
      <span>Company</span>
      <span>Street</span>
      <span>City, State/Province, Zip/Postal Code</span>
    </address>
    <address class="address address--recipient">
      <span>Jane Jones</span>
      <span>Account Number</span>
      <span>Street</span>
      <span>City, State/Province, Zip/Postal Code</span>
    </address>
    <div class="brand-motif" role="img" aria-label="Brand dot motif in grey and light blue"></div>
  </main>
</body>
</html>
```